Health & Nutrition - Business Cards

Needs to look new-age, simple, and elegant. The cards are for my services/counsel in health and nutrition - which include mind, body, and soul. I would like to see something clean and simple but beautiful. Can have a plain background or with a pattern but I don't want it to take away from my contact details. Therefore, my info can be on the back of the card and a nice front design. I really like the flower of life symbol. The name of my business is called Velvet Meadow.

Target Market(s)

Clients - men & women age 20-60. Adults, parents, teachers, sick individuals seeking nutrient counseling and dietary management.

Industry/Entity Type

Nutritionist

Contact Information for Business Card

Tomas Brindle
Cell: 345-827-4602
Email: tbrindle@quillpost.example

Colors
33a6d7
33b8a4
add136
ffffff
5c5c5c
f04a50
fbee3f
cedeed
85cae6

Requirements
Nice to have
• Maybe it can have some sort of sacred geometry as well, but not required. Nice to have the colors that I choose in the project but feel free to come up with your own use of colors. Thanks! =)

```html
<!DOCTYPE html>
<html lang="en">
<head>
<meta charset="utf-8">
<title>Velvet Meadow – Business Cards</title>
<link rel="stylesheet" href="https://fonts.googleapis.com/css2?family=Montserrat:wght@500&family=Oswald:wght@500&display=swap">
<style>
  :root {
    --backdrop: #474747;
    --card-lime: #add136;
    --mark-green: #175e46;
    --mark-soft: #2f7a5c;
    --rule-blue: #34507a;
    --ink: #3b3b3b;
    --tab: #3f3f3f;
    --white: #ffffff;
  }
  html, body {
    margin: 0;
    padding: 0;
    width: 1200px;
    height: 1000px;
    overflow: hidden;
    background: var(--backdrop);
  }
  .stage {
    position: relative;
    width: 1200px;
    height: 1000px;
  }
  .card {
    position: absolute;
    top: 156px;
    height: 701px;
    background: var(--card-lime);
    box-shadow: 4px 5px 6px rgba(0, 0, 0, 0.45);
    overflow: hidden;
  }
  .card--front { left: 160px; width: 410px; }
  .card--back  { left: 652px; width: 408px; }

  .divider {
    position: absolute;
    left: 0;
    width: 100%;
    height: 12px;
  }
  .card--front .divider { top: 376px; }
  .card--back  .divider { top: 225px; }

  .brand-dot {
    position: absolute;
    width: 204px;
    height: 204px;
    border-radius: 50%;
    background: radial-gradient(circle at 40% 38%, var(--mark-soft), var(--mark-green) 70%);
  }
  .card--front .brand-dot { left: 100px; top: 242px; }
  .card--back  .brand-dot { left: 99px;  top: 92px; }

  .brand-name {
    position: absolute;
    left: 0;
    width: 100%;
    margin: 0;
    text-align: center;
    font-family: "Montserrat", sans-serif;
    font-weight: 500;
    font-size: 28px;
    letter-spacing: 4px;
    text-transform: uppercase;
    color: var(--mark-green);
  }
  .card--front .brand-name { top: 474px; }
  .card--back  .brand-name { top: 324px; }

  .contact {
    position: absolute;
    left: 0;
    top: 540px;
    width: 100%;
    font-family: "Oswald", sans-serif;
    font-weight: 500;
    color: var(--ink);
    text-transform: uppercase;
    letter-spacing: 1px;
  }
  .contact__name {
    position: absolute;
    left: 54px;
    top: 0;
    margin: 0;
    font-size: 27px;
    line-height: 36px;
  }
  .contact__row {
    position: absolute;
    left: 0;
    display: flex;
    align-items: center;
    height: 36px;
  }
  .contact__row--phone { top: 40px; }
  .contact__row--email { top: 80px; }
  .contact__icon {
    width: 48px;
    height: 22px;
    background: var(--tab);
    display: flex;
    align-items: center;
    justify-content: flex-end;
    padding-right: 6px;
    box-sizing: border-box;
    margin-right: 6px;
  }
  .contact__value { font-size: 27px; line-height: 36px; }
  .contact__row--email .contact__value { font-size: 22px; }
</style>
</head>
<body>
<main class="stage">
  <section class="card card--front">
    <svg class="divider" viewBox="0 0 410 12" aria-hidden="true">
      <g stroke="var(--rule-blue)" stroke-width="2" fill="none">
        <line x1="0" y1="3" x2="8" y2="3"/>
        <line x1="14" y1="3" x2="88" y2="3"/>
        <line x1="18" y1="8" x2="88" y2="8"/>
        <line x1="316" y1="3" x2="392" y2="3"/>
        <line x1="398" y1="3" x2="410" y2="3"/>
        <line x1="316" y1="8" x2="386" y2="8"/>
      </g>
    </svg>
    <div class="brand-dot" aria-hidden="true"></div>
    <p class="brand-name">Velvet Meadow</p>
  </section>

  <section class="card card--back">
    <svg class="divider" viewBox="0 0 408 12" aria-hidden="true">
      <g stroke="var(--rule-blue)" stroke-width="2" fill="none">
        <line x1="0" y1="3" x2="8" y2="3"/>
        <line x1="14" y1="3" x2="87" y2="3"/>
        <line x1="18" y1="8" x2="87" y2="8"/>
        <line x1="315" y1="3" x2="390" y2="3"/>
        <line x1="396" y1="3" x2="408" y2="3"/>
        <line x1="315" y1="8" x2="384" y2="8"/>
      </g>
    </svg>
    <div class="brand-dot" aria-hidden="true"></div>
    <p class="brand-name">Velvet Meadow</p>

    <div class="contact">
      <p class="contact__name">Tomas Brindle</p>
      <div class="contact__row contact__row--phone">
        <span class="contact__icon">
          <svg width="20" height="16" viewBox="0 0 20 16" aria-label="Phone">
            <path d="M2 5 Q10 -1 18 5 L16 7 L13 6 L13 4 Q10 3 7 4 L7 6 L4 7 Z" fill="#fff"/>
            <rect x="5" y="8" width="10" height="7" rx="1" fill="#fff"/>
          </svg>
        </span>
        <span class="contact__value">345-827-4602</span>
      </div>
      <div class="contact__row contact__row--email">
        <span class="contact__icon">
          <svg width="20" height="14" viewBox="0 0 20 14" aria-label="Email">
            <rect x="0.5" y="0.5" width="19" height="13" fill="#fff"/>
            <path d="M1 1 L10 8 L19 1" fill="none" stroke="#3f3f3f" stroke-width="1.2"/>
          </svg>
        </span>
        <span class="contact__value">tbrindle@quillpost.example</span>
      </div>
    </div>
  </section>
</main>
</body>
</html>
```